Marlowick APP redesign and color change

I am looking for a new design for my app. Please see the attached current design.

Currently, I have a functioning app but the colors and design are awful!
The logo is great but the rest of the app needs a refresh.
(Logo hi res not yet available but will upload soon.)
New colors or anything that is cutting edge.

Basically: It is a secure social media app within a school system where the teachers, students and parents can text, exchange photos, plan curriculum, etc.

I NEED ONLY landing page with a new look!
Looking for one distinct design for the landing page with new look.
The developer will apply this one design towards the rest of the pages/app screens.

Because part of the social media I need the feel and look of what is now the trend. Something that will attract and keep the client(s) interested. I am really leaving all the creative work to the designer and open to any suggestions.
Updates

Target Market(s)

Schools, community, teachers, students, colleges, sport teams

Industry/Entity Type

Non Profit

Font styles to use
Serif
Sans Serif

Colors

Designer to choose colors to be used in the design.

Requirements
Must have
• Sharp, trendy, millennial feel
Nice to have
• Up to designer
Should not have
• Up to designer

```html
<!DOCTYPE html>
<html lang="en">
<head>
<meta charset="UTF-8">
<title>Marlowick — Log In</title>
<link rel="stylesheet" href="https://fonts.googleapis.com/css2?family=Montserrat:wght@300;400;600;700&display=swap">
<style>
  :root {
    --bg-night: #2c2e3b;
    --accent-blue: #79a9d3;
    --text-white: #ffffff;
    --text-muted: #5c5f6e;
    --rule: #464958;
    --footer-white: #ffffff;
    --footer-text: #2c2e3b;
    --band-mid: #9a9ca5;
    --band-light: #d3d4d8;
  }
  * { margin: 0; padding: 0; box-sizing: border-box; }
  html, body { width: 675px; height: 1200px; overflow: hidden; }
  body {
    font-family: "Montserrat", Arial, sans-serif;
    background: var(--bg-night);
    color: var(--text-white);
    position: relative;
  }
  .status-bar {
    position: absolute; top: 0; left: 0; width: 675px; height: 46px;
    font-size: 19px; font-weight: 400;
  }
  .status-signal { position: absolute; left: 13px; top: 13px; display: flex; align-items: center; gap: 3px; }
  .status-signal .dot { width: 9px; height: 9px; border-radius: 50%; border: 1.2px solid var(--text-white); }
  .status-signal .dot.full { background: var(--text-white); }
  .status-signal svg { margin-left: 6px; }
  .status-time { position: absolute; top: 12px; width: 100%; text-align: center; }
  .status-battery { position: absolute; right: 14px; top: 10px; display: flex; align-items: center; gap: 8px; }
  .battery-shell { width: 40px; height: 18px; border: 1.5px solid var(--text-white); border-radius: 3px; padding: 2px; position: relative; }
  .battery-shell::after { content: ""; position: absolute; right: -4px; top: 5px; width: 2px; height: 6px; background: var(--text-white); }
  .battery-level { width: 42%; height: 100%; background: var(--text-white); border-radius: 1px; }

  .brand-name {
    position: absolute; top: 182px; left: 0; width: 675px; text-align: center;
    font-size: 50px; font-weight: 400; letter-spacing: 0.42em; text-indent: 0.42em;
    color: var(--accent-blue);
  }

  .field { position: absolute; left: 36px; width: 603px; }
  .field-label { font-size: 21px; font-weight: 700; letter-spacing: 0.01em; line-height: 26px; }
  .field-input {
    margin-top: 38px; height: 56px; border-bottom: 2px solid var(--rule);
    font-size: 27px; font-weight: 400; line-height: 34px;
    display: flex; align-items: flex-start; justify-content: space-between;
  }
  .field-input.placeholder { color: var(--text-muted); font-weight: 300; }
  .field-username { top: 363px; }
  .field-password { top: 557px; }
  .eye-icon { margin-top: 0; margin-right: -3px; }

  .login-button {
    position: absolute; left: 36px; top: 729px; width: 603px; height: 86px;
    background: var(--accent-blue); border-radius: 4px;
    display: flex; align-items: center; justify-content: center;
    font-size: 22px; font-weight: 600; color: var(--bg-night); letter-spacing: 0.02em;
  }
  .forgot-link {
    position: absolute; top: 852px; width: 675px; text-align: center;
    font-size: 27px; font-weight: 400;
  }

  .footer-band {
    position: absolute; left: 0; top: 985px; width: 675px; height: 85px;
    background: linear-gradient(to bottom, var(--bg-night) 0%, var(--band-mid) 30%, var(--band-light) 70%, var(--footer-white) 100%);
  }
  .footer {
    position: absolute; left: 0; top: 1070px; width: 675px; height: 130px;
    background: var(--footer-white);
  }
  .signup-link {
    position: absolute; top: 1117px; width: 675px; text-align: center;
    font-size: 22px; font-weight: 600; color: var(--footer-text); letter-spacing: 0.02em;
  }
</style>
</head>
<body>
  <div class="status-bar">
    <div class="status-signal">
      <span class="dot full"></span><span class="dot full"></span><span class="dot full"></span><span class="dot"></span><span class="dot"></span>
      <svg width="20" height="15" viewBox="0 0 20 15" fill="none" stroke="#ffffff" stroke-width="2.2" stroke-linecap="round">
        <path d="M2 5 Q10 -1 18 5"/><path d="M5 8.5 Q10 4.5 15 8.5"/><circle cx="10" cy="12.5" r="1.4" fill="#ffffff" stroke="none"/>
      </svg>
    </div>
    <div class="status-time">9:41 AM</div>
    <div class="status-battery"><span>42%</span><div class="battery-shell"><div class="battery-level"></div></div></div>
  </div>

  <h1 class="brand-name">MARLOWICK</h1>

  <div class="field field-username">
    <div class="field-label">USERNAME</div>
    <div class="field-input">jmarsden27@postbox.net</div>
  </div>

  <div class="field field-password">
    <div class="field-label">PASSWORD</div>
    <div class="field-input placeholder">
      <span>Enter PIN number</span>
      <svg class="eye-icon" width="46" height="34" viewBox="0 0 46 34" fill="none" stroke="#ffffff" stroke-width="2">
        <path d="M2 17 Q23 -6 44 17 Q23 40 2 17 Z"/>
        <circle cx="23" cy="17" r="8"/>
      </svg>
    </div>
  </div>

  <div class="login-button">LOG IN</div>
  <div class="forgot-link">Forgot Password?</div>

  <div class="footer-band" role="img" aria-label="Soft grey layered wave band fading into the white footer"></div>
  <div class="footer"></div>
  <div class="signup-link">SIGN UP FOR MARLOWICK</div>
</body>
</html>
```